New Company Business Card Design

I have a new company logo and I want a new business card design. I dont know if the logo file i attached is in the correct format or quality. Precision building for demanding urban sites, delivered safely, on schedule and built to last. I want a simple and classy business card that people will his card is as crisp as the work his company does.

Target Market(s)

Clients in the heavy construction industry in New York City

Industry/Entity Type

Construction Company

Contact Information for Business Card

Simple Classy - DIFFERENT

Font styles to use
Other font styles liked:
• Mach the logo font in some way

Colors

Designer to choose colors to be used in the design.

Requirements
Must have
• Uniqueness
Nice to have
• Nothing particular - Just different and classy - Timeless
Should not have
• Goofy Shit or Gimmicky shit

```html
<!DOCTYPE html>
<html lang="en">
<head>
<meta charset="utf-8">
<title>KRT Associates, Inc. – Business Card</title>
<link href="https://fonts.googleapis.com/css2?family=Arimo:wght@400;700&display=swap" rel="stylesheet">
<style>
  :root {
    --backdrop: #3a3a3c;
    --card: #ffffff;
    --card-shade: #eef0f2;
    --brand-blue: #1b7fc4;
    --deep-blue: #1d5a9c;
    --ink: #222222;
    --rule: #555555;
    --black: #111111;
  }
  * { box-sizing: border-box; margin: 0; padding: 0; }
  html, body { width: 1200px; height: 997px; overflow: hidden; }
  body {
    background: var(--backdrop);
    font-family: "Arimo", Arial, sans-serif;
    color: var(--ink);
    position: relative;
  }
  .card {
    position: absolute;
    top: 344px;
    width: 540px;
    height: 309px;
    background: linear-gradient(160deg, var(--card) 40%, var(--card-shade));
    overflow: hidden;
  }
  .card--back { left: 40px; }
  .card--front { left: 620px; }
  .card__bands { position: absolute; left: 0; top: 0; width: 540px; height: 309px; }

  .brand {
    position: absolute;
    display: flex;
    align-items: center;
    gap: 10px;
  }
  .brand__mark { width: 18px; height: 18px; background: var(--brand-blue); }
  .brand__name {
    font-weight: 700;
    font-size: 28px;
    color: var(--brand-blue);
    letter-spacing: 1px;
    white-space: nowrap;
  }

  /* back */
  .card--back .brand { left: 0; right: 0; top: 92px; justify-content: center; }
  .tagline {
    position: absolute;
    top: 160px; left: 0; right: 0;
    text-align: center;
    font-weight: 700;
    font-size: 15px;
    line-height: 20px;
    color: var(--deep-blue);
  }
  .card--back .web {
    position: absolute;
    left: 26px; bottom: 14px;
    color: #fff;
  }
  .web {
    font-weight: 700;
    font-size: 15px;
    letter-spacing: 4px;
  }

  /* front */
  .card--front .brand { left: 150px; top: 48px; }
  .card--front .rule {
    position: absolute;
    left: 150px; right: 30px; top: 112px;
    height: 1px; background: var(--rule);
  }
  .person { position: absolute; left: 30px; top: 150px; }
  .person__name { font-weight: 700; font-size: 17px; color: var(--deep-blue); }
  .person__title { font-size: 14px; margin-top: 2px; }
  .contacts { position: absolute; left: 30px; top: 202px; list-style: none; }
  .contacts li {
    display: flex; align-items: center; gap: 10px;
    font-size: 14px; height: 20px;
  }
  .contacts svg { width: 15px; height: 15px; }
  .address {
    position: absolute; right: 26px; top: 190px;
    text-align: right; font-size: 13px; line-height: 17px;
  }
  .card--front .web {
    position: absolute;
    right: 24px; bottom: 20px;
    color: #fff;
  }
</style>
</head>
<body>

  <section class="card card--back" aria-label="Business card back">
    <svg class="card__bands" viewBox="0 0 540 309" aria-hidden="true">
      <path d="M540,292 L310,292 C290,292 290,256 265,256 L0,256 L0,309 L540,309 Z" fill="var(--brand-blue)"/>
      <path d="M540,281 L318,281 C302,281 298,262 280,260 L278,260" fill="none" stroke="var(--black)" stroke-width="5"/>
    </svg>
    <div class="brand">
      <span class="brand__mark"></span>
      <span class="brand__name">KRT ASSOCIATES, INC.</span>
    </div>
    <p class="tagline">Precision building for demanding urban sites,<br>delivered safely, on schedule and built to last.</p>
    <p class="web">www.krtbuild.com</p>
  </section>

  <section class="card card--front" aria-label="Business card front">
    <svg class="card__bands" viewBox="0 0 540 309" aria-hidden="true">
      <path d="M0,292 L230,292 C250,292 250,252 275,252 L540,252 L540,309 L0,309 Z" fill="var(--brand-blue)"/>
      <path d="M0,281 L222,281 C238,281 242,262 260,258 L262,258" fill="none" stroke="var(--black)" stroke-width="5"/>
    </svg>
    <div class="brand">
      <span class="brand__mark"></span>
      <span class="brand__name">KRT ASSOCIATES, INC.</span>
    </div>
    <div class="rule"></div>
    <div class="person">
      <p class="person__name">Marco L. Benedetti</p>
      <p class="person__title">Director &amp; Business Adviser</p>
    </div>
    <ul class="contacts">
      <li>
        <svg viewBox="0 0 16 16" aria-hidden="true"><circle cx="8" cy="8" r="8" fill="var(--deep-blue)"/><path d="M4.5,9.5 h7 v2 h-7 z M5,9 C5,5 11,5 11,9" fill="#fff"/></svg>
        <span>908-555-0147</span>
      </li>
      <li>
        <svg viewBox="0 0 16 16" aria-hidden="true"><circle cx="8" cy="8" r="8" fill="var(--deep-blue)"/><rect x="4" y="5.5" width="8" height="5.5" fill="#fff"/><path d="M4,5.5 L8,8.8 L12,5.5" fill="none" stroke="var(--deep-blue)" stroke-width="1"/></svg>
        <span>917-555-0182</span>
      </li>
      <li>
        <svg viewBox="0 0 16 16" aria-hidden="true"><circle cx="8" cy="8" r="8" fill="var(--deep-blue)"/><path d="M5,11 L11,5" stroke="#fff" stroke-width="1.6"/><circle cx="5.5" cy="10.5" r="1.6" fill="none" stroke="#fff" stroke-width="1.2"/><circle cx="10.5" cy="5.5" r="1.6" fill="none" stroke="#fff" stroke-width="1.2"/></svg>
        <span>marco@krtbuild.com</span>
      </li>
    </ul>
    <p class="address">215 Dock Street - Linden<br>New Jersey 07036</p>
    <p class="web">www.krtbuild.com</p>
  </section>

</body>
</html>
```